We Buy Houses Website

Looking for a highly motivated and skillfull designer to design and code me a "we Buy Houses" type website. I have a potential logo, but if you think you can make a BETTER one, please do try and incorporate it in your template. I am looking for creativity, professionalism, simple yet elegant. I will need a simple form on the front of the template along with pictures I provide you of recent houses I have bought. Look at these sites for examples of the layout of the website:

http://www.brickwaleholdings.example/
http://www.marlowtakesplots.example/
http://www.quickdwellingexit.example/

If you make me a design that blows me away, and you are dependable, you will become part of my team and in charge of the web aspect which will include designing, updating, any and all graphics and logo work, SEO, coding. If you have skills in all of these areas please make me a design and lets do business!! The name of the website will be "Tovin Takes Homes" at TovinTakesHomes.example

I have uploaded some pictures of houses that we have done, please feel free to incorporate this into the banner or the design, etc. I want them to know we buy houses in ANY condition, as is, cash, can close immediately so they can get on with their life. We have many options to help them find a solution to whatever problem they have. We are in the business of helping people.

Target Market(s)

People looking to sell their houses
people facing foreclosure, bankruptcy, death in the family, divorce, anyone that we can help
people with ugly houses that need a lot of repair

Industry/Entity Type

Business

Font styles to use
Serif
Sans Serif

Colors

Designer to choose colors to be used in the design.

Requirements
Must have
• must have a simple form on the front of the page, preferrably near the banner, with the few required fields to help someone get started putting in their interest to sell their house, view the 2 websites i put as examples to see what kind of fields it should have.

My phone number (555) 481-7720 along with a Tovin Takes Homes logo, clean simple and elegant and professional. I want a nice color scheme that is not white but professional and has a wow factor.

```html
<!DOCTYPE html>
<html lang="en">
<head>
<meta charset="utf-8">
<title>Tovin Takes Homes — Sell Your House Fast</title>
<link href="https://fonts.googleapis.com/css2?family=Lato:wght@300;400;700;900&display=swap" rel="stylesheet">
<style>
:root{
  --navy:#030a22;
  --navy-soft:#0b1430;
  --lime:#a6d22c;
  --lime-deep:#8fb821;
  --lime-pale:#c3e36a;
  --white:#ffffff;
  --muted:#d9e7b5;
  --ink:#1d2a0a;
}
*{box-sizing:border-box;margin:0;padding:0}
html,body{width:1200px;height:2773px;overflow:hidden}
body{font-family:'Lato',Arial,sans-serif;color:var(--white);background:var(--navy);position:relative}
.abs{position:absolute}
section,header,footer{position:absolute;left:0;width:1200px}

/* header */
.site-header{top:0;height:157px;background:var(--navy);border-top:3px solid var(--lime)}
.brand{left:185px;top:50px;display:flex;align-items:center;gap:12px}
.brand-square{width:34px;height:34px;background:var(--lime)}
.brand-name{font-size:27px;font-weight:700;color:var(--lime);letter-spacing:.3px}
.callout{left:895px;top:12px;font-size:11px;font-weight:700}
.callout-number{left:895px;top:30px;display:flex;align-items:center;gap:8px;color:var(--lime);font-size:15px}
.main-nav{right:183px;top:72px;display:flex;gap:20px;font-size:12px}
.main-nav a{color:var(--white);text-decoration:none;padding-bottom:7px}
.main-nav a.active{color:var(--lime);border-bottom:2px solid var(--lime)}

/* hero */
.hero{top:157px;height:413px;overflow:hidden}
.hero-photo{position:absolute;inset:0;background:linear-gradient(180deg,#8f96a2 0%,#7d7d7c 38%,#6e6454 62%,#5d5340 100%)}
.hero-shade{position:absolute;inset:0;background:rgba(3,10,34,.28)}
.hero-title{left:183px;top:110px;font-size:27px;font-weight:400}
.hero-rule{left:183px;top:157px;width:246px;height:2px;background:var(--lime)}
.hero-text{left:183px;top:176px;width:560px;font-size:18px;font-weight:700;line-height:32px;white-space:nowrap}
.slide-arrow{top:190px;width:26px;height:26px;background:rgba(3,10,34,.55);display:flex;align-items:center;justify-content:center}
.slide-dots{left:481px;top:396px;display:flex;gap:4px}
.slide-dots span{width:76px;height:3px;background:rgba(255,255,255,.55)}
.slide-dots span.on{background:var(--white)}
.offer-form{left:760px;top:37px;width:252px;height:329px;background:rgba(166,210,44,.88);border:3px solid rgba(195,227,106,.9);padding:0 30px}
.offer-head{height:40px;margin-top:14px;margin-bottom:22px;display:flex;align-items:center}
.offer-head h3{font-size:15px;font-weight:700;line-height:17px}
.field{display:block;width:100%;height:26px;border:1px solid rgba(255,255,255,.55);background:transparent;color:var(--white);font:400 9px 'Lato',sans-serif;padding-left:10px;margin-bottom:13px;line-height:24px}
.field-row{display:flex;gap:12px}
.field-row .field{width:50%}
.submit{height:26px;background:rgba(255,255,255,.45);text-align:center;font-size:9px;line-height:26px;letter-spacing:.5px;margin-top:8px}

/* common section headings */
.section-title{left:0;width:1200px;text-align:center;font-size:18px;font-weight:700}
.title-rule{left:578px;width:44px;height:2px;background:var(--white)}

/* how it works */
.how{top:570px;height:414px;background:var(--lime)}
.step{width:214px;text-align:center}
.step-icon{width:96px;height:96px;border-radius:50%;background:var(--lime-deep);margin:0 auto;display:flex;align-items:center;justify-content:center}
.step-name{margin-top:30px;font-size:12px;font-weight:700}
.step-note{margin-top:17px;font-size:11px;color:var(--muted)}

/* houses */
.houses{top:984px;height:549px;overflow:hidden}
.houses-photo{position:absolute;inset:0;background:linear-gradient(180deg,#1a2236 0%,#141b2e 55%,#0e1424 100%)}
.houses-shade{position:absolute;inset:0;background:rgba(3,10,34,.55)}
.house-list{font-size:11px;list-style:none}
.house-list li{display:flex;align-items:center;gap:20px;height:39px}
.tick{width:15px;height:15px;border:1px solid var(--lime);border-radius:50%;display:flex;align-items:center;justify-content:center;flex:none}
.feature-shot{left:612px;top:166px;width:405px;height:209px;background:linear-gradient(180deg,#a9b9c8 0%,#9aa1a2 45%,#6f6448 75%,#7c6a44 100%)}
.thumbs{left:612px;top:397px;display:flex;gap:6px}
.thumbs div{width:63px;height:61px}
.thumb-nav{top:480px;width:18px;height:18px;background:var(--white);display:flex;align-items:center;justify-content:center}

/* testimonials */
.testimonials{top:1533px;height:359px;background:var(--lime)}
.quote-text{left:200px;width:800px;top:144px;text-align:center;font-size:11px;font-weight:700;line-height:18.5px;white-space:nowrap}
.quote-mark{font-size:34px;font-weight:900;line-height:1}
.client{left:558px;top:236px;display:flex;align-items:center;gap:18px;font-size:11px;line-height:18px}
.client-avatar{width:36px;height:36px;border-radius:50%;background:#d6d6d2;border:2px solid var(--white)}
.client-role{color:var(--muted)}

/* articles */
.articles{top:1892px;height:549px;background:var(--navy)}
.article{width:263px;text-align:center}
.article-image{height:150px}
.article-title{margin-top:20px;font-size:13px;font-weight:400}
.article-body{margin-top:14px;font-size:11px;line-height:18.5px}
.article-meta{margin-top:22px;border-top:1px solid #1b2440;padding-top:16px;display:flex;justify-content:space-between;font-size:10px}
.meta-item{display:flex;align-items:center;gap:6px}

/* footer */
.site-footer{top:2441px;height:288px;background:linear-gradient(180deg,#9fca26 0%,#a6d22c 100%)}
.foot-col{top:30px;width:190px;font-size:9px;line-height:13px}
.foot-col h4{font-size:12px;font-weight:400;display:flex;align-items:center;gap:8px;margin-bottom:26px}
.post{display:flex;gap:10px;margin-bottom:15px}
.post-thumb{width:48px;height:40px;flex:none}
.post-date{color:var(--muted)}
.news-row{display:flex;gap:6px;margin-top:18px}
.news-field{width:156px;height:22px;border:1px solid rgba(255,255,255,.6);padding-left:8px;line-height:20px}
.news-btn{width:24px;height:22px;border:1px solid rgba(255,255,255,.6);text-align:center;line-height:20px}
.contact-line{display:flex;align-items:center;gap:8px;margin-top:6px}
.bottom-bar{top:2729px;height:44px;background:var(--navy);font-size:9px}
.copyright{left:183px;top:16px}
.social{right:183px;top:11px;display:flex;gap:12px}
.social span{width:22px;height:22px;border:1px solid var(--lime)}
</style>
</head>
<body>

<header class="site-header">
  <div class="brand abs"><span class="brand-square"></span><span class="brand-name">Tovin Takes Homes</span></div>
  <div class="callout abs">Call Now:</div>
  <div class="callout-number abs">
    <svg width="12" height="12" viewBox="0 0 24 24"><path d="M6.6 10.8a15 15 0 0 0 6.6 6.6l2.2-2.2c.3-.3.7-.4 1-.2 1.1.4 2.3.6 3.6.6.6 0 1 .4 1 1V20c0 .6-.4 1-1 1A17 17 0 0 1 3 4c0-.6.4-1 1-1h3.5c.6 0 1 .4 1 1 0 1.3.2 2.5.6 3.6.1.3 0 .7-.2 1z" fill="#a6d22c"/></svg>
    (555) 481-7720
  </div>
  <nav class="main-nav abs">
    <a class="active">Home</a><a>About</a><a>How It Works</a><a>Sell a House</a><a>Testimonials</a><a>Blog</a><a>Contact</a>
  </nav>
</header>

<section class="hero">
  <div class="hero-photo" role="img" aria-label="Photo of a single-storey house with a garage and front yard"></div>
  <div class="hero-shade"></div>
  <h1 class="hero-title abs">Sell Your House Fast</h1>
  <div class="hero-rule abs"></div>
  <p class="hero-text abs">Selling your house can be simple, let us show you how<br>we have changed the way you can sell your house.</p>
  <div class="slide-arrow abs" style="left:89px"><svg width="8" height="12" viewBox="0 0 8 12"><path d="M6 1 1 6l5 5" stroke="#fff" stroke-width="2" fill="none"/></svg></div>
  <div class="slide-arrow abs" style="left:1084px"><svg width="8" height="12" viewBox="0 0 8 12"><path d="M2 1l5 5-5 5" stroke="#fff" stroke-width="2" fill="none"/></svg></div>
  <div class="slide-dots abs"><span class="on"></span><span></span><span></span></div>

  <form class="offer-form abs">
    <div class="offer-head">
      <h3>Get An Offer<br>On Your House</h3>
    </div>
    <div class="field">Name</div>
    <div class="field">Phone Number</div>
    <div class="field">Your Email</div>
    <div class="field">Property Adress</div>
    <div class="field-row"><div class="field">City</div><div class="field">Zip Code</div></div>
    <div class="submit">SUBMIT</div>
  </form>
</section>

<section class="how">
  <h2 class="section-title abs" style="top:86px">How It Works</h2>
  <div class="title-rule abs" style="top:117px"></div>

  <svg class="abs" style="left:330px;top:150px" width="560" height="120" viewBox="0 0 560 120">
    <path d="M10 108 C40 110 60 100 80 88" stroke="#fff" stroke-width="1.5" fill="none"/><path d="M72 86l9 1-3 8" stroke="#fff" stroke-width="1.5" fill="none"/>
    <path d="M215 20 C250 0 285 6 305 30" stroke="#fff" stroke-width="1.5" fill="none"/><path d="M297 29l9 2 0-9" stroke="#fff" stroke-width="1.5" fill="none"/>
    <path d="M435 112 C470 112 490 104 510 90" stroke="#fff" stroke-width="1.5" fill="none"/><path d="M502 88l9 1-3 8" stroke="#fff" stroke-width="1.5" fill="none"/>
  </svg>

  <div class="step abs" style="left:172px;top:162px">
    <div class="step-icon"><svg width="40" height="40" viewBox="0 0 40 40"><path d="M8 32l3-10 17-17 7 7-17 17z" fill="#5a8fd6"/><path d="M8 32l3-10 7 7z" fill="#f2d49b"/></svg></div>
    <div class="step-name">Complete the Form</div><div class="step-note">We evaluate your property instantly.</div>
  </div>
  <div class="step abs" style="left:385px;top:162px">
    <div class="step-icon"><svg width="40" height="40" viewBox="0 0 40 40"><rect x="12" y="4" width="16" height="32" rx="3" fill="#fff"/><rect x="14" y="8" width="12" height="22" fill="#1d2a0a"/></svg></div>
    <div class="step-name">Get a Call within 24 Hours</div><div class="step-note">We can discuss your best options.</div>
  </div>
  <div class="step abs" style="left:599px;top:162px">
    <div class="step-icon"><svg width="40" height="40" viewBox="0 0 40 40"><circle cx="20" cy="16" r="10" fill="#f6d03a"/><rect x="15" y="26" width="10" height="8" fill="#e0e0e0"/></svg></div>
    <div class="step-name">Find a Solution</div><div class="step-note">Sell your house fast.</div>
  </div>
  <div class="step abs" style="left:812px;top:162px">
    <div class="step-icon"><svg width="44" height="30" viewBox="0 0 44 30"><rect x="2" y="4" width="40" height="22" fill="#e9f2df"/><rect x="6" y="8" width="32" height="14" fill="#7aa663"/><circle cx="22" cy="15" r="5" fill="#e9f2df"/></svg></div>
    <div class="step-name">Go On With Your Life</div><div class="step-note">Find the relief you deserve.</div>
  </div>
</section>

<section class="houses">
  <div class="houses-photo" role="img" aria-label="Dusk photo of a house, darkened as section background"></div>
  <div class="houses-shade"></div>
  <h2 class="section-title abs" style="top:86px">Houses that we buy</h2>
  <div class="title-rule abs" style="top:117px;background:var(--lime)"></div>

  <ul class="house-list abs" style="left:183px;top:167px">
    <li><span class="tick"><svg width="6" height="8" viewBox="0 0 6 8"><path d="M1 1l4 3-4 3" stroke="#a6d22c" fill="none"/></svg></span>Normal Homes</li>
    <li><span class="tick"><svg width="6" height="8" viewBox="0 0 6 8"><path d="M1 1l4 3-4 3" stroke="#a6d22c" fill="none"/></svg></span>Vacant Homes</li>
    <li><span class="tick"><svg width="6" height="8" viewBox="0 0 6 8"><path d="M1 1l4 3-4 3" stroke="#a6d22c" fill="none"/></svg></span>Needs Repairs</li>
    <li><span class="tick"><svg width="6" height="8" viewBox="0 0 6 8"><path d="M1 1l4 3-4 3" stroke="#a6d22c" fill="none"/></svg></span>Needs Extensive Renovation</li>
    <li><span class="tick"><svg width="6" height="8" viewBox="0 0 6 8"><path d="M1 1l4 3-4 3" stroke="#a6d22c" fill="none"/></svg></span>Has Suffered Storm Damage</li>
    <li><span class="tick"><svg width="6" height="8" viewBox="0 0 6 8"><path d="M1 1l4 3-4 3" stroke="#a6d22c" fill="none"/></svg></span>Undesirable Neighborhood</li>
    <li><span class="tick"><svg width="6" height="8" viewBox="0 0 6 8"><path d="M1 1l4 3-4 3" stroke="#a6d22c" fill="none"/></svg></span>Bad Tenants</li>
  </ul>
  <ul class="house-list abs" style="left:398px;top:167px">
    <li><span class="tick"><svg width="6" height="8" viewBox="0 0 6 8"><path d="M1 1l4 3-4 3" stroke="#a6d22c" fill="none"/></svg></span>Code Violations</li>
    <li><span class="tick"><svg width="6" height="8" viewBox="0 0 6 8"><path d="M1 1l4 3-4 3" stroke="#a6d22c" fill="none"/></svg></span>Relocation Or Emigration</li>
    <li><span class="tick"><svg width="6" height="8" viewBox="0 0 6 8"><path d="M1 1l4 3-4 3" stroke="#a6d22c" fill="none"/></svg></span>Has Become Too Ugly To Sell</li>
  </ul>

  <div class="feature-shot abs" role="img" aria-label="Photo of a bought house with a dry front lawn"></div>
  <div class="thumbs abs">
    <div role="img" aria-label="Kitchen interior photo" style="background:#8a6a45"></div>
    <div role="img" aria-label="Room interior photo" style="background:#9c8070"></div>
    <div role="img" aria-label="Overgrown yard photo" style="background:#6f7256"></div>
    <div role="img" aria-label="Empty room photo" style="background:#b39a7e"></div>
    <div role="img" aria-label="Bathroom photo" style="background:#4a4a52"></div>
    <div role="img" aria-label="Backyard grass photo" style="background:#8f8a5c"></div>
  </div>
  <div class="thumb-nav abs" style="left:974px"><svg width="6" height="8" viewBox="0 0 6 8"><path d="M5 1 1 4l4 3" stroke="#030a22" stroke-width="1.5" fill="none"/></svg></div>
  <div class="thumb-nav abs" style="left:999px"><svg width="6" height="8" viewBox="0 0 6 8"><path d="M1 1l4 3-4 3" stroke="#030a22" stroke-width="1.5" fill="none"/></svg></div>
</section>

<section class="testimonials">
  <h2 class="section-title abs" style="top:86px">Testimonials</h2>
  <div class="title-rule abs" style="top:117px"></div>
  <span class="quote-mark abs" style="left:232px;top:136px">&ldquo;</span>
  <p class="quote-text abs">Phasellus varius felis magna, id dapibus dui luctus et. Nam molestie ac eros sed eleifend. Etiam porttitor varius venenatis. Integer<br>dui ante, euismod sed condimentum sit amet, lobortis et enim. Proin in felis ornare, aliquet justo non, feugiat dui.<br>Sed consequat odio quis faucibus rutrum. Vestibulum porta nunc tellus, in lacinia nisi malesuada sed.</p>
  <span class="quote-mark abs" style="left:898px;top:186px">&rdquo;</span>
  <svg class="abs" style="left:508px;top:246px" width="10" height="16" viewBox="0 0 10 16"><path d="M8 2 2 8l6 6" stroke="#fff" stroke-width="2" fill="none"/></svg>
  <svg class="abs" style="left:708px;top:246px" width="10" height="16" viewBox="0 0 10 16"><path d="M2 2l6 6-6 6" stroke="#fff" stroke-width="2" fill="none"/></svg>
  <div class="client abs">
    <div class="client-avatar" role="img" aria-label="Client portrait"></div>
    <div>John Doe<br><span class="client-role">Client</span></div>
  </div>
</section>

<section class="articles">
  <h2 class="section-title abs" style="top:86px">Latest Articles</h2>
  <div class="title-rule abs" style="top:117px;background:var(--lime)"></div>

  <article class="article abs" style="left:183px;top:164px">
    <div class="article-image" role="img" aria-label="Photo of a house with a dry lawn" style="background:linear-gradient(180deg,#a7b6c6 0%,#8d8b84 55%,#7a6a48 100%)"></div>
    <h3 class="article-title">Proin venenatis leo dui</h3>
    <p class="article-body">Praesent elementum faucibus sapien. Nunc blandit tellus et odio volutpat elementum sed ut turpis. Praesent sit amet varius sem.</p>
    <div class="article-meta">
      <span class="meta-item"><svg width="10" height="10" viewBox="0 0 10 10"><circle cx="5" cy="5" r="4" stroke="#a6d22c" fill="none"/><path d="M5 3v2h2" stroke="#a6d22c" fill="none"/></svg>18 June 2014</span>
      <span class="meta-item"><svg width="10" height="10" viewBox="0 0 10 10"><path d="M1 9l1-3 5-5 2 2-5 5z" fill="#a6d22c"/></svg>Admin</span>
      <span class="meta-item"><svg width="12" height="10" viewBox="0 0 12 10"><path d="M1 1h10v6H5L2 9V7H1z" fill="#a6d22c"/></svg>2 Comments</span>
    </div>
  </article>
  <article class="article abs" style="left:468px;top:164px">
    <div class="article-image" role="img" aria-label="Photo of a covered patio and overgrown yard" style="background:linear-gradient(180deg,#5c5a52 0%,#7c8064 50%,#6a6249 100%)"></div>
    <h3 class="article-title">Proin venenatis leo dui</h3>
    <p class="article-body">Praesent elementum faucibus sapien. Nunc blandit tellus et odio volutpat elementum sed ut turpis. Praesent sit amet varius sem.</p>
    <div class="article-meta">
      <span class="meta-item"><svg width="10" height="10" viewBox="0 0 10 10"><circle cx="5" cy="5" r="4" stroke="#a6d22c" fill="none"/><path d="M5 3v2h2" stroke="#a6d22c" fill="none"/></svg>18 June 2014</span>
      <span class="meta-item"><svg width="10" height="10" viewBox="0 0 10 10"><path d="M1 9l1-3 5-5 2 2-5 5z" fill="#a6d22c"/></svg>Admin</span>
      <span class="meta-item"><svg width="12" height="10" viewBox="0 0 12 10"><path d="M1 1h10v6H5L2 9V7H1z" fill="#a6d22c"/></svg>2 Comments</span>
    </div>
  </article>
  <article class="article abs" style="left:753px;top:164px">
    <div class="article-image" role="img" aria-label="Photo of a bathroom interior" style="background:linear-gradient(180deg,#6b5a6a 0%,#3e3a44 50%,#8a8684 100%)"></div>
    <h3 class="article-title">Proin venenatis leo dui</h3>
    <p class="article-body">Praesent elementum faucibus sapien. Nunc blandit tellus et odio volutpat elementum sed ut turpis. Praesent sit amet varius sem.</p>
    <div class="article-meta">
      <span class="meta-item"><svg width="10" height="10" viewBox="0 0 10 10"><circle cx="5" cy="5" r="4" stroke="#a6d22c" fill="none"/><path d="M5 3v2h2" stroke="#a6d22c" fill="none"/></svg>18 June 2014</span>
      <span class="meta-item"><svg width="10" height="10" viewBox="0 0 10 10"><path d="M1 9l1-3 5-5 2 2-5 5z" fill="#a6d22c"/></svg>Admin</span>
      <span class="meta-item"><svg width="12" height="10" viewBox="0 0 12 10"><path d="M1 1h10v6H5L2 9V7H1z" fill="#a6d22c"/></svg>2 Comments</span>
    </div>
  </article>
</section>

<footer class="site-footer">
  <div class="foot-col abs" style="left:183px">
    <h4>About <svg width="12" height="12" viewBox="0 0 12 12"><circle cx="6" cy="4" r="3" fill="#fff"/><path d="M1 12a5 5 0 0 1 10 0z" fill="#fff"/></svg></h4>
    <p>Mauris gravida, nibh at vulputate mattis, diam urna aliquam ante, sit amet blandit magna dui sed nisl. Phasellus interdum sollicitudin euismod. Vestibulum a tortor eleifend, luctus purus sit, placerat leo.</p>
  </div>
  <div class="foot-col abs" style="left:396px">
    <h4>Latest Posts <svg width="12" height="12" viewBox="0 0 12 12"><path d="M1 11l1-3 6-6 2 2-6 6z" fill="#fff"/></svg></h4>
    <div class="post"><div class="post-thumb" role="img" aria-label="House photo" style="background:#8a8a70"></div><div>Proin venenatis<br>leo dui<br><span class="post-date">Posted 18 June 2014</span></div></div>
    <div class="post"><div class="post-thumb" role="img" aria-label="Patio photo" style="background:#6c6a58"></div><div>Suspendisse sed<br>aliquet ante<br><span class="post-date">Posted 18 June 2014</span></div></div>
    <div class="post"><div class="post-thumb" role="img" aria-label="Bathroom photo" style="background:#5e5360"></div><div>Lorem ipsum dolor<br>sit amet<br><span class="post-date">Posted 18 June 2014</span></div></div>
  </div>
  <div class="foot-col abs" style="left:610px">
    <h4>Newsletter <svg width="12" height="12" viewBox="0 0 12 12"><path d="M1 6 11 1 7 11 6 7z" fill="#fff"/></svg></h4>
    <p>Phasellus interdum sollicitudin euismod. Vestibulum a tortor eleifend, luctus purus sit, placerat leo.</p>
    <div class="news-row"><div class="news-field">Email adress...</div><div class="news-btn">OK</div></div>
  </div>
  <div class="foot-col abs" style="left:823px">
    <h4>Get in Touch <svg width="14" height="12" viewBox="0 0 14 12"><path d="M1 1h10v6H5L2 10V7H1z" fill="#fff"/></svg></h4>
    <p>Tovin Takes Homes<br>2210 Harbor Lane, Suite B4<br>Oakview, CA 90210</p>
    <div class="contact-line"><svg width="9" height="9" viewBox="0 0 24 24"><path d="M6.6 10.8a15 15 0 0 0 6.6 6.6l2.2-2.2c.3-.3.7-.4 1-.2 1.1.4 2.3.6 3.6.6.6 0 1 .4 1 1V20c0 .6-.4 1-1 1A17 17 0 0 1 3 4c0-.6.4-1 1-1h3.5c.6 0 1 .4 1 1 0 1.3.2 2.5.6 3.6.1.3 0 .7-.2 1z" fill="#fff"/></svg>(555) 481-7720</div>
    <div class="contact-line"><svg width="10" height="8" viewBox="0 0 10 8"><rect x=".5" y=".5" width="9" height="7" fill="none" stroke="#fff"/><path d="M.5.5 5 4 9.5.5" stroke="#fff" fill="none"/></svg>contact@tovintakes.example</div>
  </div>
</footer>

<div class="bottom-bar abs" style="left:0;width:1200px">
  <div class="copyright abs">&copy;2014 Tovin Takes Homes - All Rights Reserved. &nbsp;&nbsp; Privacy policy &nbsp;|&nbsp; Terms of services</div>
  <div class="social abs"><span></span><span></span><span></span><span></span></div>
</div>

</body>
</html>
```